23rd Annual Harrowgate Lantern Film Festival Poster

Design an eye catchy, stylish poster for our 23rd film festival. Be different not just a poster with a film reel. Think outside of the box with a design that will attract peoples attention. Colorful (you choose the colors). Make it fun and creative, like the film festival. Show your talents in the design. Be sure it is new and stylish. Dates are August 21 - 29, 2020. Poster size will be 27 inches by 40 inches

Target Market(s)

Upper Middle class - movie lovers

Font styles to use
Sans Serif

Colors
33a6d7

Requirements
Must have
• NO CLIP ART - be original !
Nice to have
• abstract - think outside the box
Should not have
• CLIP ART

```html
<!DOCTYPE html>
<html lang="en">
<head>
<meta charset="utf-8">
<title>23rd Annual Harrowgate Lantern Film Festival — August 21 – 29, 2020</title>
<link rel="stylesheet" href="https://fonts.googleapis.com/css2?family=Montserrat:wght@300;400&family=Teko:wght@300&display=swap">
<style>
  :root {
    --ink: #121416;
    --accent: #33a6d7;
    --accent-glow: rgba(51, 166, 215, 0.38);
    --wall-dark: #2b2d2f;
    --wall-mid: #5f6468;
    --wall-light: #b7c3c9;
    --edge: #34373a;
  }
  html, body {
    margin: 0;
    padding: 0;
    width: 810px;
    height: 1200px;
    overflow: hidden;
    background: var(--wall-dark);
  }
  .poster {
    position: relative;
    width: 810px;
    height: 1200px;
    overflow: hidden;
  }
  .backdrop {
    position: absolute;
    inset: 0;
    background:
      linear-gradient(90deg, rgba(0,0,0,0) 0%, rgba(0,0,0,0) 94%, var(--edge) 97.5%, #26282a 100%),
      repeating-linear-gradient(180deg, rgba(255,255,255,0) 0px, rgba(255,255,255,0.10) 40px, rgba(255,255,255,0) 80px),
      radial-gradient(ellipse 55% 60% at 72% 48%, var(--accent-glow), rgba(51,166,215,0) 72%),
      radial-gradient(ellipse 60% 55% at 70% 45%, rgba(225,232,236,0.45), rgba(225,232,236,0) 70%),
      linear-gradient(90deg, var(--wall-dark) 0%, #44484b 30%, var(--wall-mid) 50%, var(--wall-light) 78%, #a7b2b8 92%);
  }
  .title { margin: 0; }
  .letter {
    position: absolute;
    transform: translate(-50%, -50%);
    font-family: "Montserrat", sans-serif;
    font-weight: 300;
    font-size: 46px;
    line-height: 1;
    color: var(--ink);
  }
  .letter--bar {
    width: 3px;
    height: 32px;
    background: var(--accent);
  }
  .edition {
    position: absolute;
    left: 406px;
    top: 1098px;
    transform: translate(-50%, -50%);
    margin: 0;
    font-family: "Montserrat", sans-serif;
    font-weight: 400;
    font-size: 16px;
    letter-spacing: 7px;
    text-transform: uppercase;
    color: var(--accent);
    white-space: nowrap;
  }
  .dates {
    position: absolute;
    left: 406px;
    top: 1154px;
    transform: translate(-50%, -50%);
    margin: 0;
    font-family: "Teko", sans-serif;
    font-weight: 300;
    font-size: 52px;
    line-height: 1;
    color: var(--ink);
    white-space: nowrap;
  }
</style>
</head>
<body>
<main class="poster">
  <div class="backdrop" role="img" aria-label="Blurred photograph of soft window light falling across a grey-blue wall"></div>

  <h1 class="title" aria-label="Harrowgate Lantern Film Festival">
    <span class="letter" style="left:122px;top:165px">H</span>
    <span class="letter" style="left:190px;top:96px">A</span>
    <span class="letter" style="left:242px;top:216px">R</span>
    <span class="letter" style="left:318px;top:234px">R</span>
    <span class="letter" style="left:348px;top:148px">O</span>
    <span class="letter" style="left:390px;top:184px">W</span>
    <span class="letter" style="left:459px;top:184px">G</span>
    <span class="letter" style="left:534px;top:286px">A</span>
    <span class="letter letter--bar" style="left:574px;top:318px"></span>
    <span class="letter" style="left:626px;top:302px">E</span>

    <span class="letter letter--bar" style="left:64px;top:419px"></span>
    <span class="letter" style="left:158px;top:464px">L</span>
    <span class="letter" style="left:242px;top:398px">A</span>
    <span class="letter" style="left:346px;top:404px">N</span>
    <span class="letter" style="left:428px;top:408px">T</span>
    <span class="letter" style="left:495px;top:450px">E</span>
    <span class="letter" style="left:408px;top:560px">R</span>
    <span class="letter" style="left:562px;top:593px">N</span>

    <span class="letter" style="left:176px;top:722px">F</span>
    <span class="letter letter--bar" style="left:290px;top:708px"></span>
    <span class="letter" style="left:390px;top:754px">L</span>
    <span class="letter" style="left:510px;top:706px">M</span>

    <span class="letter" style="left:145px;top:884px">F</span>
    <span class="letter" style="left:200px;top:950px">E</span>
    <span class="letter" style="left:272px;top:880px">S</span>
    <span class="letter" style="left:273px;top:1034px">T</span>
    <span class="letter letter--bar" style="left:362px;top:928px"></span>
    <span class="letter" style="left:458px;top:970px">V</span>
    <span class="letter" style="left:562px;top:902px">A</span>
    <span class="letter" style="left:628px;top:952px">L</span>
  </h1>

  <p class="edition">23rd Annual</p>
  <p class="dates">August 21 – 29, 2020</p>
</main>
</body>
</html>
```